Wine Bottle Label Graphic Design (mini bottle 187ml)

Looking for a contemporary custom wine label design for party favors. Inspiration photos provided. **Please see "wine favorite" example in uploads.

Artwork 2.5" wide by 2.75" tall to be placed on 3"x3" stickers. Specs from printer attached but I still want image to fit within the artwork size I specified. Please make label center justified. This is for BOYS. It does not need to be super "masculine"...but definitely not feminine.

Required elements:

Colors: white background, include gold and purple to match logo. Other colors are fine to include.

Name: Toviah 13 (I like use of the No) as shown in the sample, but not required
Varietal: Mitzvah Blend 6.11.2021
Vineyard: Brockel Family Vineyard
Location: Maryland
Logo: See attached (KRNotecard Final)

Serif
Sans Serif

• All the above elements. Clean and crisp design. Contemporary and classy. Purple, Gold, Black colors. See logo. You CAN include cursive font for select elements. I don't mind a combination of print and script.
• Floral, scrolling, background image, old fashioned

```html
<!DOCTYPE html>
<html lang="en">
<head>
<meta charset="utf-8">
<title>Toviah 13 – Mitzvah Blend label concepts</title>
<link rel="stylesheet" href="https://fonts.googleapis.com/css2?family=Alfa+Slab+One&family=Bebas+Neue&family=Cinzel:wght@400;600&family=Montserrat:wght@500;600&family=Playfair+Display:wght@500;700&family=Yellowtail&display=swap">
<style>
  :root {
    --purple: #46307c;
    --purple-deep: #3a2569;
    --gold: #d4a72c;
    --gold-light: #f6e7a6;
    --gold-dark: #b98a1f;
    --ink: #111111;
    --paper: #ffffff;
    --badge: #cfae22;
    --gold-sheen: linear-gradient(100deg, #f2b705 0%, #f8eeb0 22%, #d9a93a 48%, #b8852a 66%, #f3e3a0 100%);
    --gold-soft: linear-gradient(90deg, #e6b94a 0%, #f7e9b5 35%, #d2a23d 70%, #f0d98f 100%);
  }
  * { box-sizing: border-box; margin: 0; padding: 0; }
  html, body { width: 1200px; height: 716px; overflow: hidden; background: var(--paper); }
  .stage {
    position: relative; width: 1250px; height: 746px;
    transform: scale(0.96); transform-origin: 0 0;
  }
  .label {
    position: absolute; top: 122px; width: 346px; height: 381px;
    background: var(--paper); overflow: hidden; border-radius: 4px;
    box-shadow: 0 2px 6px rgba(0,0,0,.18);
    text-align: center;
  }
  .label--a { left: 67px; }
  .label--b { left: 456px; }
  .label--c { left: 852px; }

  .band { position: absolute; left: 0; width: 100%; }
  .band--purple { background: var(--purple); }
  .band--gold { background: var(--gold-sheen); }
  .band--gold-line { background: var(--gold-soft); }
  .band--pattern { background: var(--gold-soft); }

  .crest {
    position: absolute; left: 50%; width: 122px; height: 122px; margin-left: -61px;
    border-radius: 50%; background: var(--purple);
    box-shadow: 0 0 0 4px var(--paper);
    display: flex; align-items: center; justify-content: center;
  }
  .crest__name {
    font-family: "Cinzel", serif; font-weight: 600; font-size: 13px;
    line-height: 1.35; letter-spacing: 1px; color: var(--paper);
  }

  .line { position: absolute; left: 0; width: 100%; white-space: nowrap; }

  /* Concept A */
  .a-title { top: 160px; font-family: "Bebas Neue", sans-serif; font-size: 70px; line-height: 1; color: var(--ink); }
  .a-varietal { top: 230px; font-family: "Cinzel", serif; font-weight: 600; font-size: 14px; letter-spacing: 4px; color: var(--purple); }
  .a-year { top: 257px; font-family: "Cinzel", serif; font-size: 11px; letter-spacing: 2px; color: var(--ink); }
  .a-vineyard { top: 290px; font-family: "Cinzel", serif; font-size: 13px; letter-spacing: 2px; color: var(--purple); }
  .a-place { top: 316px; font-family: "Cinzel", serif; font-size: 9px; letter-spacing: 2.5px; color: var(--ink); }

  /* Concept B */
  .b-title { top: 44px; font-family: "Alfa Slab One", serif; font-size: 42px; line-height: 1; color: var(--purple); }
  .b-varietal { top: 248px; font-family: "Montserrat", sans-serif; font-weight: 600; font-size: 17px; letter-spacing: 3px; color: var(--purple); }
  .b-year { top: 270px; font-family: "Montserrat", sans-serif; font-weight: 500; font-size: 11px; letter-spacing: 1.5px; color: var(--ink); }
  .b-vineyard { top: 294px; font-family: "Yellowtail", cursive; font-size: 20px; color: var(--purple); }
  .b-place { top: 320px; font-family: "Montserrat", sans-serif; font-weight: 600; font-size: 10px; letter-spacing: 3px; color: var(--ink); }

  /* Concept C */
  .c-title { top: 166px; font-family: "Playfair Display", serif; font-weight: 500; font-size: 54px; line-height: 1; color: var(--purple); }
  .c-block { left: auto; right: 38px; width: auto; text-align: center; }
  .c-varietal { top: 249px; font-family: "Cinzel", serif; font-weight: 600; font-size: 14px; letter-spacing: 3.5px; color: var(--purple); }
  .c-year { top: 268px; font-family: "Cinzel", serif; font-size: 11px; letter-spacing: 2px; color: var(--ink); right: 41px; }
  .c-vineyard { top: 285px; font-family: "Yellowtail", cursive; font-size: 19px; color: var(--purple); right: 37px; }
  .c-place { top: 317px; font-family: "Cinzel", serif; font-size: 9px; letter-spacing: 2.5px; color: var(--ink); right: 38px; }

  .option {
    position: absolute; top: 602px; width: 54px; height: 54px; border-radius: 50%;
    background: var(--badge); color: var(--ink);
    font-family: "Playfair Display", serif; font-weight: 700; font-size: 28px;
    display: flex; align-items: center; justify-content: center;
  }
  .option--a { left: 209px; }
  .option--b { left: 609px; }
  .option--c { left: 1024px; }
</style>
</head>
<body>
<main class="stage">

  <section class="label label--a" aria-label="Label concept A">
    <div class="band band--purple" style="top:0;height:81px"></div>
    <div class="band band--gold-line" style="top:81px;height:9px"></div>
    <div class="crest" style="top:20px"><p class="crest__name">KADEN &amp;<br>REUBEN</p></div>
    <h2 class="line a-title">TOVIAH 13</h2>
    <p class="line a-varietal">MITZVAH BLEND</p>
    <p class="line a-year">2021</p>
    <p class="line a-vineyard">BROCKEL FAMILY VINEYARD</p>
    <p class="line a-place">MARYLAND</p>
    <div class="band band--purple" style="top:335px;height:9px"></div>
    <div class="band band--gold" style="top:344px;height:37px"></div>
  </section>

  <section class="label label--b" aria-label="Label concept B">
    <div class="band band--pattern" style="top:0;height:23px" role="img" aria-label="Gold wavy line pattern border"></div>
    <div class="band band--purple" style="top:23px;height:5px"></div>
    <h2 class="line b-title">Toviah 13</h2>
    <div class="crest" style="top:108px"><p class="crest__name">KADEN &amp;<br>REUBEN</p></div>
    <p class="line b-varietal">MITZVAH BLEND</p>
    <p class="line b-year">2021</p>
    <p class="line b-vineyard">Brockel Family Vineyard</p>
    <p class="line b-place">MARYLAND</p>
    <div class="band band--purple" style="top:335px;height:9px"></div>
    <div class="band band--pattern" style="top:344px;height:37px" role="img" aria-label="Gold wavy line pattern border"></div>
  </section>

  <section class="label label--c" aria-label="Label concept C">
    <div class="band band--purple" style="top:0;height:81px;background:linear-gradient(180deg,var(--purple),var(--purple-deep))" role="img" aria-label="Purple fine line texture"></div>
    <div class="band band--gold-line" style="top:81px;height:9px"></div>
    <div class="crest" style="top:20px"><p class="crest__name">KADEN &amp;<br>REUBEN</p></div>
    <h2 class="line c-title">TOVIAH 13</h2>
    <p class="line c-block c-varietal">MITZVAH BLEND</p>
    <p class="line c-block c-year">2021</p>
    <p class="line c-block c-vineyard">Brockel Family Vineyard</p>
    <p class="line c-block c-place">MARYLAND</p>
    <div class="band band--purple" style="top:335px;height:9px"></div>
    <div class="band band--pattern" style="top:344px;height:37px" role="img" aria-label="Gold fine line pattern border"></div>
  </section>

  <span class="option option--a">A</span>
  <span class="option option--b">B</span>
  <span class="option option--c">C</span>

</main>
</body>
</html>
```